Postcard Design

Hoofmere Ftness Center is a state of the art equine rehabilitation and fitness center. We offer a wide variety of options to get your equine partner in tip top performing condition. Whether is swimming in or 11 foot deep pool or exercising in the squatted, we provide a personalized program for your special horse. Some other services offered are StallAir breathing treatments, pulso drift and gallotone.
Updates
Project Deadline Extended Reason: Since the project was started we have opened for business and I have pictures using my equipment at our place of business that I would like to add to the project to be used. I have also received my logo design from one of your designers that I would like added to this project. Added Tuesday, March 15, 2016
Industry/Entity Type
Fitness
Look and feel
Each slider illustrates characteristics of the customer's brand and the style your logo design should communicate.

```html
<!DOCTYPE html>
<html lang="en">
<head>
<meta charset="utf-8">
<title>Hoofmere Fitness Center – Postcard</title>
<link rel="stylesheet" href="https://fonts.googleapis.com/css2?family=Didact+Gothic&family=Old+Standard+TT&display=swap">
<style>
  :root {
    --ink: #050505;
    --page: #ffffff;
    --sky: #8ec5df;
    --gold: #e5b526;
    --gold-line: #c9a44a;
    --gold-light: #e8d08a;
    --paper-text: #e9e9e9;
    --accent-text: #e3a64a;
    --link-blue: #8fc3e6;
  }
  * { box-sizing: border-box; margin: 0; padding: 0; }
  html, body { width: 1200px; height: 786px; overflow: hidden; background: var(--page); }
  body { position: relative; font-family: "Didact Gothic", "Century Gothic", sans-serif; }

  .postcard {
    position: absolute; top: 29px; width: 557px; height: 728px;
    background: var(--ink); overflow: hidden;
  }
  .postcard--front { left: 29px; }
  .postcard--back { left: 613px; }

  .brand-name {
    position: absolute; text-align: center; font-weight: 400; line-height: 1;
  }
  .brand-name__line1 { display: block; color: var(--sky); font-size: 46px; letter-spacing: 5px; }
  .brand-name__line2 { display: block; color: var(--gold); font-size: 31px; margin-top: 6px; letter-spacing: 0.5px; }
  .postcard--front .brand-name { left: 38px; top: 38px; width: 292px; }
  .postcard--back .brand-name { left: 60px; top: 52px; width: 292px; }

  .brand-art {
    position: absolute; left: 332px; top: 17px; width: 225px; height: 164px;
    background: radial-gradient(ellipse at 55% 50%, #e9722b 0%, #8a3fa8 35%, #2aa6b4 65%, #0a0a0a 100%);
  }
  .postcard--back .brand-art { left: 347px; top: 19px; width: 210px; height: 148px; }

  .contact-top { position: absolute; left: 38px; width: 292px; text-align: center; color: var(--paper-text); }
  .contact-top__phone { top: 145px; font-size: 23px; }
  .contact-top__email { top: 176px; font-size: 16px; }
  .icon { display: inline-block; vertical-align: middle; }

  .photo {
    position: absolute; left: 0; top: 200px; width: 557px; height: 510px;
    background: linear-gradient(170deg, #cfd7d2 0%, #9fb7ad 25%, #3fc4c6 50%, #2c2a2b 65%, #59d0cf 80%, #d9f2f0 100%);
  }
  .waves { position: absolute; left: 0; top: 0; width: 557px; height: 728px; }

  .copy {
    position: absolute; left: 55px; top: 206px; width: 468px;
    color: var(--paper-text); font-size: 17.5px; line-height: 24.5px; letter-spacing: 0.3px;
  }
  .copy p { margin-bottom: 21px; }
  .copy .lead-name { font-style: italic; }
  .drop-cap {
    float: left; font-family: "Old Standard TT", Georgia, serif;
    font-size: 54px; line-height: 42px; margin: 5px 4px 0 0; color: #f4f4f4;
  }
  .call-to-action {
    position: absolute; left: 0; top: 500px; width: 557px; text-align: center;
    color: var(--accent-text); font-style: italic; font-size: 17px; line-height: 26px;
  }
  .contact-row {
    position: absolute; left: 32px; top: 574px; width: 500px;
    display: flex; justify-content: space-between; align-items: baseline; color: var(--link-blue);
  }
  .contact-row__phone { font-size: 24px; text-decoration: underline; text-underline-offset: 4px; }
  .contact-row__email { font-size: 18px; text-decoration: underline; }
  .address {
    position: absolute; left: 0; top: 610px; width: 557px; text-align: center;
    color: var(--link-blue); font-size: 18px;
  }
</style>
</head>
<body>

<section class="postcard postcard--front">
  <div class="photo" role="img" aria-label="Photo of a dark bay horse swimming in a turquoise pool, led on a line by a handler"></div>
  <svg class="waves" viewBox="0 0 557 728" aria-hidden="true">
    <path d="M0 190 H557 V205 C420 200 250 215 0 285 Z" fill="var(--ink)"/>
    <path d="M0 282 C250 212 420 202 557 210" fill="none" stroke="var(--gold-line)" stroke-width="5"/>
    <path d="M0 290 C240 225 420 215 557 222" fill="none" stroke="var(--gold-light)" stroke-width="1.5"/>
    <path d="M0 620 C140 650 280 735 557 690 V728 H0 Z" fill="var(--ink)"/>
    <path d="M0 625 C150 655 290 730 557 685" fill="none" stroke="var(--gold-line)" stroke-width="5"/>
    <path d="M0 640 C150 675 300 745 557 700" fill="none" stroke="var(--gold-light)" stroke-width="1.5"/>
  </svg>
  <h1 class="brand-name"><span class="brand-name__line1">HOOFMERE</span><span class="brand-name__line2">FITNESS CENTER</span></h1>
  <div class="brand-art" role="img" aria-label="Colourful rainbow-striped horse head illustration"></div>
  <p class="contact-top contact-top__phone">
    <svg class="icon" width="18" height="18" viewBox="0 0 18 18" aria-hidden="true"><circle cx="9" cy="9" r="7.5" fill="none" stroke="currentColor" stroke-width="1.4"/><path d="M6 5 L8 7 L7 8.5 C8 10 8.5 10.5 9.5 11 L11 10 L13 12 L11.5 13.5 C8 13 5 10 4.5 6.5 Z" fill="currentColor"/></svg>
    361-555-0148</p>
  <p class="contact-top contact-top__email">
    <svg class="icon" width="16" height="11" viewBox="0 0 16 11" aria-hidden="true"><rect x="0.7" y="0.7" width="14.6" height="9.6" fill="none" stroke="currentColor" stroke-width="1.3"/><path d="M1 1 L8 6 L15 1" fill="none" stroke="currentColor" stroke-width="1.3"/></svg>
    hoofmerefit@example.com</p>
</section>

<section class="postcard postcard--back">
  <svg class="waves" viewBox="0 0 557 728" aria-hidden="true">
    <path d="M0 150 C150 160 300 175 557 135" fill="none" stroke="var(--gold-line)" stroke-width="4"/>
    <path d="M0 162 C180 178 330 182 557 150" fill="none" stroke="var(--gold-light)" stroke-width="1.5"/>
    <path d="M0 145 C160 150 330 170 557 120" fill="none" stroke="var(--gold-line)" stroke-width="1.2"/>
    <path d="M0 640 C150 670 300 725 557 680" fill="none" stroke="var(--gold-line)" stroke-width="5"/>
    <path d="M0 652 C160 685 320 740 557 695" fill="none" stroke="var(--gold-light)" stroke-width="1.5"/>
    <path d="M250 708 C380 712 470 706 557 668" fill="none" stroke="var(--gold-line)" stroke-width="2"/>
  </svg>
  <h1 class="brand-name"><span class="brand-name__line1">HOOFMERE</span><span class="brand-name__line2">FITNESS CENTER</span></h1>
  <div class="brand-art" role="img" aria-label="Colourful rainbow-striped horse head illustration"></div>

  <div class="copy">
    <p><span class="drop-cap">H</span><span class="lead-name">oofmere Ftness Center</span> is a state of the art equine rehabilitation and fitness center. We offer a wide variety of options to get your equine partner in tip top performing condition.</p>
    <p><span class="drop-cap">W</span>hether is swimming in 11 foot deep pool or exercising in the squatted, we provide a personalized program for your special horse.</p>
    <p><span class="drop-cap">S</span>ome other services offered are StallAir breathing treatments, pulso drift and gallotone.</p>
  </div>

  <p class="call-to-action">Please contact us for more information<br>or to make an appointment:</p>
  <div class="contact-row">
    <span class="contact-row__phone">
      <svg class="icon" width="18" height="18" viewBox="0 0 18 18" aria-hidden="true"><circle cx="9" cy="9" r="7.5" fill="none" stroke="currentColor" stroke-width="1.4"/><path d="M6 5 L8 7 L7 8.5 C8 10 8.5 10.5 9.5 11 L11 10 L13 12 L11.5 13.5 C8 13 5 10 4.5 6.5 Z" fill="currentColor"/></svg>
      361-555-0148</span>
    <span class="contact-row__email">
      <svg class="icon" width="16" height="11" viewBox="0 0 16 11" aria-hidden="true"><rect x="0.7" y="0.7" width="14.6" height="9.6" fill="none" stroke="currentColor" stroke-width="1.3"/><path d="M1 1 L8 6 L15 1" fill="none" stroke="currentColor" stroke-width="1.3"/></svg>
      hoofmerefit@example.com</span>
  </div>
  <p class="address">4180 Willow Bend Road, Marlow Springs, TX 78000</p>
</section>

</body>
</html>
```